NEED A BUSINESS CARD FOR A NEW ELECTRICAL BUSINESS

HI I am after a new business card for my new electrical business I have a logo that I have attached its the one in blue, I would like that on the front and on the back my name- Leonard Pike, Email leonardpike@tallmesh.com, mobile 0491362047, licence no# vic 47819, nsw 591304k I wont something that is a stand out from the rest but at the same time is neat as being a new business I wont it to catch peoples eye on the front of the card I would like the logo and not much else.
And on the back as well I would like a slogan saying something like
Quality-Reliable-Service

Hi all on the back of the card I would like a little slogan like Quality-Reliable-Service something like that would be good thanks

Hi all the business card needs to have both these licence numbers on it                                                  VIC-47819 nsw-591304k

```html
<!DOCTYPE html>
<html lang="en">
<head>
<meta charset="utf-8">
<title>Leonard Pike Electrical – Business Card</title>
<link rel="stylesheet" href="https://fonts.googleapis.com/css2?family=Michroma&family=Arimo:wght@700&display=swap">
<style>
  :root {
    --backdrop: #e6e4e1;
    --card-top: #2c2f34;
    --card-bottom: #14161a;
    --brand-blue: #1f63c6;
    --rule-blue: #1d5fd0;
    --contact-blue: #2a6fd6;
  }
  * { box-sizing: border-box; margin: 0; padding: 0; }
  html, body {
    width: 1200px;
    height: 675px;
    overflow: hidden;
    background: var(--backdrop);
  }
  .canvas {
    width: 1200px;
    height: 675px;
    display: flex;
    justify-content: center;
    align-items: center;
    gap: 60px;
  }
  .card {
    position: relative;
    width: 300px;
    height: 520px;
    background: linear-gradient(160deg, var(--card-top) 0%, var(--card-bottom) 100%);
    box-shadow: 0 10px 28px rgba(0, 0, 0, 0.25);
    overflow: hidden;
  }
  .wordmark {
    font-family: "Michroma", sans-serif;
    font-weight: 400;
    color: var(--brand-blue);
    text-transform: uppercase;
    text-align: center;
    line-height: 1.25;
    white-space: nowrap;
  }
  .wordmark .wordmark-name { display: block; }
  .wordmark .wordmark-trade { display: block; }

  /* front */
  .card-front .wordmark {
    position: absolute;
    left: 0;
    right: 0;
    top: 50%;
    transform: translateY(-50%);
  }
  .card-front .wordmark-name { font-size: 22px; letter-spacing: 0.8px; }
  .card-front .wordmark-trade { font-size: 12px; letter-spacing: 3.2px; margin-top: 6px; }

  /* back */
  .card-back .wordmark {
    position: absolute;
    left: 0;
    right: 0;
    top: 34px;
  }
  .card-back .wordmark-name { font-size: 17px; letter-spacing: 0.6px; }
  .card-back .wordmark-trade { font-size: 9px; letter-spacing: 2.2px; margin-top: 4px; }
  .rule {
    position: absolute;
    left: 0;
    right: 0;
    height: 4px;
    background: var(--rule-blue);
  }
  .rule-top { top: 104px; }
  .rule-bottom { bottom: 60px; }
  .contact {
    position: absolute;
    left: 30px;
    right: 20px;
    top: 196px;
    font-family: "Arimo", sans-serif;
    font-weight: 700;
    color: var(--contact-blue);
  }
  .contact-name {
    font-size: 24px;
    margin-bottom: 10px;
  }
  .contact-line {
    font-size: 13px;
    line-height: 1.75;
  }
  .slogan {
    position: absolute;
    left: 0;
    right: 0;
    bottom: 20px;
    font-family: "Arimo", sans-serif;
    font-weight: 700;
    font-size: 13px;
    letter-spacing: 1px;
    text-align: center;
    color: var(--contact-blue);
  }
</style>
</head>
<body>
  <main class="canvas">
    <section class="card card-front" aria-label="Card front">
      <div class="wordmark">
        <span class="wordmark-name">Leonard Pike</span>
        <span class="wordmark-trade">Electrical</span>
      </div>
    </section>

    <section class="card card-back" aria-label="Card back">
      <div class="wordmark">
        <span class="wordmark-name">Leonard Pike</span>
        <span class="wordmark-trade">Electrical</span>
      </div>
      <div class="rule rule-top"></div>
      <div class="contact">
        <p class="contact-name">Leonard Pike</p>
        <p class="contact-line">leonardpike@tallmesh.com</p>
        <p class="contact-line">M: 0491362047</p>
        <p class="contact-line">VIC 47819</p>
        <p class="contact-line">NSW 591304k</p>
      </div>
      <div class="rule rule-bottom"></div>
      <p class="slogan">Quality – Reliable – Service</p>
    </section>
  </main>
</body>
</html>
```